All-Natural Head Lice Removal company

I need a business card with my pre-existing logo. We are a new company located in Portland Oregon that goes into peoples homes to help with head lice removal. My products and approach are all- natural and also will be around children.On my current logo we used Teal Bl and the color Green. I am open to new ideas just want it simple and creative

Target Market(s)

my biggest market is families of school aged children

Industry/Entity Type

Business

Contact Information for Business Card

see upload for details from previous business card

Font styles to use
Serif

Colors
33a6d7
9bcb3b
f37122

Requirements
Must have
• Basic information/ logo put into a creative format that is catching to the eye
Nice to have
• creative

```html
<!DOCTYPE html>
<html lang="en">
<head>
<meta charset="utf-8">
<title>ClearComb Business Card</title>
<link rel="stylesheet" href="https://fonts.googleapis.com/css2?family=Arvo:wght@400;700&display=swap">
<style>
  :root {
    --sky-light: #8fd6f2;
    --sky: #33a6d7;
    --sky-deep: #1f86c4;
    --leaf: #9bcb3b;
    --ink: #1c1c1e;
    --ink-soft: #2e2e31;
    --paper: #ffffff;
    --stage: #ececec;
  }
  * { box-sizing: border-box; margin: 0; padding: 0; }
  html, body { width: 1200px; height: 913px; overflow: hidden; }
  body {
    background: var(--stage);
    font-family: "Arvo", Georgia, serif;
    display: flex;
    align-items: center;
    justify-content: center;
    gap: 40px;
  }
  .card {
    position: relative;
    width: 540px;
    height: 310px;
    border-radius: 16px;
    overflow: hidden;
    box-shadow: 0 10px 26px rgba(0,0,0,.18);
  }
  .card--front { background: linear-gradient(160deg, var(--sky-light) 0%, var(--sky) 45%, var(--sky-deep) 100%); }
  .card--back { background: var(--paper); }
  .card__swoosh { position: absolute; inset: 0; width: 100%; height: 100%; }
  .brand {
    position: absolute;
    display: flex;
    align-items: center;
    gap: 10px;
  }
  .brand__dot {
    width: 56px; height: 56px;
    border-radius: 50%;
    background: var(--leaf);
  }
  .brand__name {
    font-weight: 700;
    font-size: 30px;
    color: var(--ink);
    line-height: 1;
  }
  .card--front .brand { left: 28px; top: 128px; }
  .card--back .brand { left: 50%; top: 62px; transform: translateX(-50%); }
  .contact {
    position: absolute;
    left: 300px;
    top: 40px;
    padding-left: 20px;
    border-left: 1px solid rgba(255,255,255,.55);
    color: var(--paper);
  }
  .contact__name { font-weight: 700; font-size: 17px; letter-spacing: .5px; text-transform: uppercase; }
  .contact__title { font-size: 10px; text-transform: uppercase; letter-spacing: 1px; margin-bottom: 12px; }
  .contact__row { display: flex; align-items: center; gap: 8px; font-size: 11.5px; line-height: 19px; }
  .contact__row svg { width: 10px; height: 10px; fill: var(--paper); flex: none; }
  .swoosh-text { font-family: "Arvo", Georgia, serif; font-size: 15px; }
  .swoosh-text--blue { fill: var(--sky); }
  .swoosh-text--dark { fill: var(--ink-soft); font-weight: 700; font-size: 13.5px; }
  .swoosh-text--light { fill: var(--paper); font-size: 12px; }
</style>
</head>
<body>

  <section class="card card--front">
    <svg class="card__swoosh" viewBox="0 0 540 310" aria-hidden="true">
      <path d="M0 310 L0 252 Q300 248 540 138 L540 310 Z" fill="#ffffff"/>
      <path d="M0 310 L0 257 Q300 253 540 143 L540 310 Z" fill="var(--sky)"/>
      <path d="M0 310 L0 262 Q300 258 540 148 L540 310 Z" fill="var(--ink)"/>
      <path id="front-curve" d="M0 292 Q300 288 540 178" fill="none"/>
      <text class="swoosh-text swoosh-text--blue"><textPath href="#front-curve" startOffset="9%">All Natural In-Home Lice Removal Services</textPath></text>
    </svg>

    <div class="brand">
      <span class="brand__dot"></span>
      <span class="brand__name">ClearComb</span>
    </div>

    <div class="contact">
      <p class="contact__name">Maya Holloway</p>
      <p class="contact__title">Owner</p>
      <p class="contact__row"><svg viewBox="0 0 10 10"><path d="M2 0 L4 2.5 L3 3.5 Q4.5 6 6.5 7 L7.5 6 L10 8 L8.5 10 Q2 9 0 1.5 Z"/></svg>1-800-555-0142</p>
      <p class="contact__row"><svg viewBox="0 0 10 10"><path d="M0 2 H10 V8.5 H0 Z M0.8 2.6 L5 5.6 L9.2 2.6" fill="none" stroke="#fff" stroke-width="1"/></svg>maya@clearcomb.com</p>
      <p class="contact__row"><svg viewBox="0 0 10 10"><circle cx="5" cy="5" r="5"/></svg>www.clearcomb.com</p>
    </div>
  </section>

  <section class="card card--back">
    <svg class="card__swoosh" viewBox="0 0 540 310" aria-hidden="true">
      <path d="M0 310 L0 300 Q300 275 540 150 L540 310 Z" fill="var(--sky)"/>
      <path d="M0 310 L0 306 Q300 282 540 158 L540 310 Z" fill="var(--ink)"/>
      <path id="back-line-1" d="M40 268 Q300 240 520 120" fill="none"/>
      <path id="back-line-2" d="M60 282 Q300 256 530 136" fill="none"/>
      <path id="back-web" d="M200 300 Q380 270 530 185" fill="none"/>
      <text class="swoosh-text swoosh-text--dark"><textPath href="#back-line-1" startOffset="24%">Try ClearComb Today and Be Lice Free Tomorrow!</textPath></text>
      <text class="swoosh-text swoosh-text--dark"><textPath href="#back-line-2" startOffset="24%">All Natural In-Home Lice Removal Services</textPath></text>
      <text class="swoosh-text swoosh-text--light"><textPath href="#back-web" startOffset="30%">www.clearcomb.com</textPath></text>
    </svg>

    <div class="brand">
      <span class="brand__dot"></span>
      <span class="brand__name">ClearComb</span>
    </div>
  </section>

</body>
</html>
```